Innovative approaches to treat addiction

PowerPoint on different techniques
Add graphics to screen
Easy to follow
I've provided the PowerPoint w content
Now make it pretty
And
hand outs for them to follow and take notes
Can you also add my bio:
Mara J. Thornquist, MS LCADC is a licensed Psychotherapist with a specialty in Addiction Disorders and over 22 years of clinical experience. Her integrative approach to counseling combines years of clinical experience with cognitive behavioral and traditional psychotherapy, with holistic therapies including; mindfulness, NLP, hypnotherapy, yoga therapy, reiki, motivational and wellness coaching.
Handout materials for them to follow and take notes

```html
<!DOCTYPE html>
<html lang="en">
<head>
<meta charset="utf-8">
<title>Innovative Techniques to Treat Disorders – Slide Overview</title>
<link href="https://fonts.googleapis.com/css2?family=Merriweather+Sans:wght@400;700;800&family=Open+Sans:wght@300;400;600;700&display=swap" rel="stylesheet">
<style>
:root{
  --canvas:#dcd8d9;
  --paper:#ffffff;
  --blue:#3a7bbf;
  --blue-deep:#2f6db0;
  --yellow:#e3dc2b;
  --ink:#2b2b2b;
  --muted:#9a9a9a;
  --faint:#c9c9c9;
  --ring:#d8dde3;
}
*{box-sizing:border-box;margin:0;padding:0}
html,body{width:1200px;height:1200px;overflow:hidden;background:var(--canvas)}
body{position:relative;font-family:"Open Sans",Arial,sans-serif;color:var(--ink)}
.slide{position:absolute;background:var(--paper);overflow:hidden}
.photo{position:absolute}
.corner-dot{position:absolute;top:14px;right:26px;width:9px;height:9px;border-radius:50%;background:var(--blue)}
.footer-mark{position:absolute;left:24px;bottom:8px;font-size:3.5px;color:var(--faint);font-weight:700}
.footer-mark span{font-weight:400}
.kicker{position:absolute;left:0;right:0;text-align:center;font-size:4.5px;color:var(--muted)}
.slide-title{position:absolute;left:0;right:0;text-align:center;font-size:12px;color:var(--ink)}
.title-rule{position:absolute;left:50%;width:14px;height:1px;margin-left:-7px}
.tl-line{position:absolute;height:1px;background:var(--blue)}
.node{position:absolute;width:20px;height:20px;border-radius:50%;background:var(--blue);border:2px solid #cfe0f1;color:#fff;font-size:3.6px;line-height:4px;text-align:center;display:flex;align-items:center;justify-content:center;transform:translate(-50%,-50%)}
.node.is-yellow{background:var(--yellow);border-color:#f3efa9}
.node-label{position:absolute;width:80px;margin-left:-40px;text-align:center;font-size:4.6px;font-weight:600}
.node-note{display:block;font-weight:400;font-size:3.6px;color:var(--muted);margin-top:4px;line-height:5px}
.body-copy{font-size:3.7px;line-height:6px;color:#777}
.panel-head{font-size:5.6px;font-weight:600;color:var(--ink)}
.panel-sub{font-size:3.6px;color:var(--yellow);margin-bottom:4px}
.circle-card{position:absolute;border-radius:50%;background:var(--blue)}
.circle-ring{position:absolute;border-radius:50%;background:rgba(230,232,235,.75)}
.hero-word{font-family:"Merriweather Sans","Open Sans",sans-serif;font-weight:800;color:#fff}
</style>
</head>
<body>

<!-- Row 1 -->
<section class="slide" style="left:29px;top:19px;width:346px;height:194px">
  <div class="photo" role="img" aria-label="Monochrome photograph of several women's faces layered together" style="inset:0;background:radial-gradient(circle at 45% 40%,#6b6b6b,#3a3a3a 55%,#222 100%)"></div>
  <h1 class="hero-word" style="position:absolute;left:0;right:0;top:56px;text-align:center;font-size:19px;line-height:24px;font-weight:700">Innovative Techniques to<br>Treat Disorders</h1>
  <p style="position:absolute;left:0;right:0;top:122px;text-align:center;font-size:6px;color:#bbb">Mara Thornquist</p>
  <p style="position:absolute;left:0;right:0;top:138px;text-align:center;font-size:3.4px;color:#aaa;letter-spacing:.3px">MS LCADC, CHT, 500RYT</p>
</section>

<section class="slide" style="left:418px;top:18px;width:345px;height:194px">
  <p class="kicker" style="top:10px">Insert your subtitle text here</p>
  <h2 class="slide-title" style="top:18px">New Innovative Approaches</h2>
  <div class="title-rule" style="top:36px;background:var(--yellow)"></div>
  <div class="corner-dot"></div>
  <div class="tl-line" style="left:68px;right:0;top:97px"></div>
  <svg style="position:absolute;left:26px;top:76px" width="42" height="42" viewBox="0 0 42 42" aria-hidden="true">
    <circle cx="21" cy="21" r="20" fill="#fff" stroke="#cfd4da" stroke-width="1"/>
    <path d="M13 21 L21 14 L29 21 M15 19 V28 H27 V19 M19 28 V23 H23 V28" fill="none" stroke="var(--blue)" stroke-width="1.3" stroke-linejoin="round"/>
  </svg>
  <div class="node" style="left:143px;top:97px">9:00<br>AM</div>
  <div class="node" style="left:243px;top:97px">9:15<br>AM</div>
  <p class="node-label" style="left:143px;top:113px">Increase patient retention<span class="node-note">Tools that allow people or companies to create, share</span></p>
  <p class="node-label" style="left:243px;top:113px">Increase rapport<span class="node-note">Tools that allow people or companies to create, share</span></p>
  <p class="footer-mark">Business <span>Presentation</span></p>
</section>

<section class="slide" style="left:799px;top:19px;width:348px;height:194px">
  <div class="corner-dot"></div>
  <div class="tl-line" style="left:0;right:0;top:98px"></div>
  <div class="node" style="left:54px;top:98px">9:30<br>AM</div>
  <div class="node is-yellow" style="left:168px;top:98px">10:00<br>AM</div>
  <div class="node" style="left:289px;top:98px">11:00<br>AM</div>
  <p class="node-label" style="left:54px;top:115px">Increase healing time<span class="node-note">Tools that allow people or companies to create, share</span></p>
  <p class="node-label" style="left:168px;top:115px;width:100px;margin-left:-50px">Increase compliance<br><br>with treatment recommendations</p>
  <p class="node-label" style="left:289px;top:115px">Reduce stress<span class="node-note">Tools that allow people or companies to create, share</span></p>
  <p class="footer-mark">Business <span>Presentation</span></p>
</section>

<!-- Row 2 -->
<section class="slide" style="left:29px;top:258px;width:351px;height:197px">
  <div class="corner-dot"></div>
  <div class="tl-line" style="left:0;width:246px;top:98px"></div>
  <div class="node" style="left:54px;top:98px">12:30<br>PM</div>
  <div class="node is-yellow" style="left:170px;top:98px">06:00<br>PM</div>
  <div style="position:absolute;left:245px;top:77px;width:43px;height:43px;border-radius:50%;border:1px solid #cfd4da;background:#fff;display:flex;align-items:center;justify-content:center;font-size:6px;font-weight:600">FINISH</div>
  <p class="node-label" style="left:54px;top:115px">Reduce burnout<span class="node-note">Tools that allow people or companies to create, share</span></p>
  <p class="node-label" style="left:170px;top:115px">Fun and sustainable</p>
  <p style="position:absolute;left:50px;right:50px;top:168px;text-align:center;font-size:3.4px;line-height:5.5px;color:var(--muted)">“These techniques are not a replacement of standard medical procedures, but work in conjunction with them by freeing the patient of feelings or attitudes that may be compromising his or her natural immune system.”</p>
  <p class="footer-mark">Business <span>Presentation</span></p>
</section>

<section class="slide" style="left:418px;top:258px;width:347px;height:195px">
  <p class="kicker" style="top:11px">Insert your subtitle text here</p>
  <h2 class="slide-title" style="top:19px">The Innovative Approaches</h2>
  <div class="title-rule" style="top:37px;background:var(--ink)"></div>
  <div class="corner-dot"></div>
  <div style="position:absolute;left:173px;top:48px;width:1px;height:147px;background:var(--blue)"></div>
  <svg style="position:absolute;left:0;top:0" width="347" height="195" aria-hidden="true">
    <g fill="var(--blue)"><circle cx="173.5" cy="52" r="2"/><circle cx="173.5" cy="76" r="2"/><circle cx="173.5" cy="106" r="2"/><circle cx="173.5" cy="139" r="2"/><circle cx="173.5" cy="163" r="2"/></g>
  </svg>
  <p style="position:absolute;right:192px;top:48px;font-size:6.6px;font-weight:600;color:var(--blue)">Mindfulness</p>
  <p style="position:absolute;left:192px;top:72px;font-size:6.6px;font-weight:600;color:var(--blue)">Meditation</p>
  <p style="position:absolute;right:192px;top:102px;font-size:6.6px;font-weight:600;color:#d8cf1e">Breathwork</p>
  <p style="position:absolute;left:192px;top:135px;font-size:6.6px;font-weight:600;color:var(--blue)">Asana/ Hand Mudra</p>
  <p style="position:absolute;right:204px;top:160px;text-align:right;font-size:6.6px;line-height:7.5px;font-weight:600;color:#d8cf1e">Hypnosis/ Self<br>Hypnosis</p>
  <p style="position:absolute;left:186px;top:161px;font-size:6.6px;line-height:7.5px;font-weight:600;color:var(--blue)">Neuro-linguisitic<br>Programming</p>
  <p class="footer-mark">Business <span>Presentation</span></p>
</section>

<section class="slide" style="left:799px;top:258px;width:353px;height:198px">
  <p class="kicker" style="top:11px">Insert your subtitle text here</p>
  <h2 class="slide-title" style="top:19px">Meet The Psychotherapist</h2>
  <div class="title-rule" style="top:37px;background:var(--ink)"></div>
  <div class="corner-dot"></div>
  <div class="photo" role="img" aria-label="Portrait photograph of the psychotherapist" style="left:34px;top:68px;width:67px;height:67px;background:linear-gradient(135deg,#3a2a24,#8a6a5c 55%,#2b1f1b)"></div>
  <p style="position:absolute;left:117px;top:70px;font-size:5.4px;font-weight:600">Mara J. Thornquist</p>
  <p style="position:absolute;left:117px;top:77px;font-size:3.6px;color:var(--muted)">MS LCADC</p>
  <p class="body-copy" style="position:absolute;left:117px;top:85px;width:102px;text-align:justify">A licensed Psychotherapist with a specialty in Addiction Disorders and over 22 years of clinical experience. Her integrative approach to counseling combines years of clinical experience with cognitive behavioral and traditional psychotherapy, with holistic therapies including; mindfulness, NLP, hypnotherapy, yoga therapy, reiki, motivational and wellness coaching.</p>
  <div style="position:absolute;left:227px;top:70px;width:1px;height:66px;background:#e6e6e6"></div>
  <p style="position:absolute;left:237px;top:70px;font-size:5px;font-weight:600">Skills</p>
  <p style="position:absolute;left:237px;top:77px;font-size:3.4px;color:var(--muted)">Psychotherapist</p>
  <svg style="position:absolute;left:237px;top:89px" width="90" height="40" aria-hidden="true">
    <g font-size="3" fill="#888" font-family="Open Sans, sans-serif">
      <text x="0" y="3">Speaking</text><text x="0" y="14">Leadership</text><text x="0" y="25">Social Media</text><text x="0" y="36">Marketing</text>
    </g>
    <g fill="#e7e7e7"><rect x="24" y="0" width="60" height="4"/><rect x="24" y="11" width="60" height="4"/><rect x="24" y="22" width="60" height="4"/><rect x="24" y="33" width="60" height="4"/></g>
    <rect x="24" y="0" width="41" height="4" fill="var(--blue)"/>
    <rect x="24" y="11" width="50" height="4" fill="var(--blue)"/>
    <rect x="24" y="22" width="47" height="4" fill="var(--yellow)"/>
    <rect x="24" y="33" width="50" height="4" fill="#c4ccd6"/>
  </svg>
  <p class="footer-mark">Business <span>Presentation</span></p>
</section>

<!-- Row 3 -->
<section class="slide" style="left:29px;top:490px;width:353px;height:199px">
  <div class="photo" role="img" aria-label="Photograph of a woman stretching her arm outdoors among green trees" style="inset:0;background:radial-gradient(circle at 20% 40%,#c9d98a,#7a9a3c 40%,#3f5a22 80%)"></div>
  <div class="circle-card" style="left:178px;top:18px;width:178px;height:178px"></div>
  <div style="position:absolute;left:245px;top:48px;width:68px;height:1px;background:var(--yellow)"></div>
  <p class="hero-word" style="position:absolute;right:28px;top:66px;text-align:right;font-size:22px;line-height:25px">Mind<br>fulness</p>
  <p style="position:absolute;right:26px;top:117px;width:140px;text-align:right;font-size:5.2px;line-height:6.5px;color:#e6eef8">The practice of being aware of daily experiences with the intention to create a non-judgmental state of awareness</p>
  <div style="position:absolute;left:245px;top:145px;width:68px;height:1px;background:var(--yellow)"></div>
</section>

<section class="slide" style="left:418px;top:490px;width:352px;height:198px">
  <div class="photo" role="img" aria-label="Photograph of stacked stones along a rocky shoreline" style="left:0;top:0;width:177px;height:99px;background:linear-gradient(180deg,#8f9594,#5d6562 50%,#7e8a88)"></div>
  <div class="photo" role="img" aria-label="Photograph of a dark night sky over water" style="left:177px;top:99px;width:175px;height:99px;background:linear-gradient(180deg,#1f1b2a,#3a2530 60%,#1a1420)"></div>
  <p style="position:absolute;left:177px;top:143px;width:175px;text-align:center;font-size:7px;letter-spacing:2.6px;color:#fff">MINDFULNESS</p>
  <div class="corner-dot"></div>
  <div style="position:absolute;left:190px;top:20px;width:150px">
    <p class="panel-head">Mindfulness</p>
    <p class="panel-sub">Your headline here</p>
    <p class="body-copy" style="text-align:justify">• The practice of being aware of daily experiences with the intention to create a non-judgmental state of awareness. Mindfulness teaches patients to recognize and challenge unwanted thoughts and behaviors.<br>Benefits:<br>• Prevents relapse, control cravings, control negative emotions, individual has the ability to monitor their well-being, recognize discomfort, reduces anxiety.</p>
  </div>
  <div style="position:absolute;left:42px;top:110px;width:125px;text-align:right">
    <p class="panel-head">Research:</p>
    <p class="panel-sub">Your headline here</p>
    <p class="body-copy" style="text-align:center">A university study conducted over two years followed the long term effects of mindfulness based treatment. Clients were assigned to eight weekly group sessions that used mindfulness based treatment or other types of treatment groups. Targeted mindfulness practices may support long term outcomes by strengthening the ability to monitor and skillfully cope with discomfort associated with craving or negative affect, thus supporting long term outcomes.</p>
  </div>
  <p class="footer-mark">Business <span>Presentation</span></p>
</section>

<section class="slide" style="left:799px;top:490px;width:359px;height:202px">
  <div class="photo" role="img" aria-label="Photograph of a woman meditating on a pier facing a calm sea" style="inset:0;background:linear-gradient(180deg,#cfe2ea 0%,#e9f1ef 40%,#9cc2c6 62%,#6e9fa8 100%)"></div>
  <div class="circle-ring" style="left:-40px;top:-18px;width:232px;height:232px"></div>
  <div class="circle-card" style="left:-11px;top:2px;width:200px;height:200px"></div>
  <div style="position:absolute;left:27px;top:48px;width:90px;height:1px;background:var(--yellow)"></div>
  <p class="hero-word" style="position:absolute;left:26px;top:78px;font-size:22px">Meditation</p>
  <p style="position:absolute;left:26px;top:110px;width:130px;font-size:5.2px;line-height:6.5px;color:#e6eef8">A method of achieving relaxation and consciousness by focusing on a mantras, sound, or image while eliminating outside stimuli from one's awareness.</p>
  <div style="position:absolute;left:27px;top:146px;width:90px;height:1px;background:var(--yellow)"></div>
</section>

<!-- Row 4 -->
<section class="slide" style="left:29px;top:733px;width:357px;height:201px">
  <div class="photo" role="img" aria-label="Photograph of hands resting in a meditation pose" style="left:0;top:0;width:179px;height:101px;background:linear-gradient(135deg,#efe7e0,#d9c5b7 55%,#f3eeea)"></div>
  <div class="photo" role="img" aria-label="Photograph of a group meditating on grass at sunset" style="left:179px;top:101px;width:178px;height:100px;background:radial-gradient(circle at 80% 20%,#fff3c4,#e8b24a 30%,#7f9a3b 70%,#4a6a24)"></div>
  <div class="corner-dot"></div>
  <div style="position:absolute;left:191px;top:20px;width:150px">
    <p class="panel-head">Meditation</p>
    <p class="panel-sub">Your headline here</p>
    <p class="body-copy" style="text-align:justify">• A method of achieving relaxation and consciousness by focusing on a mantras, sound, or image while eliminating outside stimuli from one's awareness.<br>• Mantra: a word or phrase repeated during meditation to remain focus and calm the body.<br>Benefits:<br>• Reduce patients physical and mental suffering, improve emotional stability and self-control, reduces mind wandering, and improves self care, create a calm environment.</p>
  </div>
  <div style="position:absolute;left:12px;top:108px;width:158px">
    <p class="panel-head" style="text-align:right">Research:</p>
    <p class="panel-sub" style="text-align:right">Your headline here</p>
    <p class="body-copy" style="text-align:justify">• A study conducted by university researchers examined adults in a meditation program. The researchers measured various states of mind wandering and evaluated them as neutral, pleasant and unpleasant topics. They also examined their caring behaviors for themselves and others. Throughout the program that lasted for nine sessions, there was a significant reduction in the participants unpleasant mind wandering, a decrease in neutral mind wandering, and a significant increase in self-care and caring behaviors for others.</p>
  </div>
  <p class="footer-mark">Business <span>Presentation</span></p>
</section>

<section class="slide" style="left:418px;top:733px;width:356px;height:201px">
  <div class="photo" role="img" aria-label="Photograph of a woman holding a yoga balance pose on a rock by the sea" style="inset:0;background:linear-gradient(180deg,#d9e1e6 0%,#eef2f3 50%,#9fb2bd 72%,#5f6b70 100%)"></div>
  <div class="circle-ring" style="left:-26px;top:-18px;width:228px;height:228px"></div>
  <div class="circle-card" style="left:-8px;top:-9px;width:192px;height:192px"></div>
  <div style="position:absolute;left:34px;top:49px;width:80px;height:1px;background:var(--yellow)"></div>
  <p class="hero-word" style="position:absolute;left:22px;top:56px;font-size:22px;line-height:28px">Yoga Asana/<br>Hand Mudra</p>
  <p style="position:absolute;left:26px;top:114px;width:138px;font-size:5.2px;line-height:6.5px;color:#e6eef8">• The physical postures of yoga replaces negative thinking and behaviors with physical movement and positive thinking.<br>• Hand Mudra's- are positions of the body, in most cases the hand, that allows for a change in mood or energy.</p>
  <div style="position:absolute;left:34px;top:162px;width:80px;height:1px;background:var(--yellow)"></div>
</section>

<section class="slide" style="left:799px;top:733px;width:359px;height:202px">
  <div class="photo" role="img" aria-label="Photograph of a woman in a downward dog yoga pose in a bright room" style="left:0;top:0;width:180px;height:101px;background:linear-gradient(135deg,#f4f2ef,#dcd6cf 55%,#c9c2c6)"></div>
  <div class="photo" role="img" aria-label="Photograph of hands forming a mudra in front of yellow flowers" style="left:180px;top:101px;width:179px;height:101px;background:linear-gradient(135deg,#3c4a1f,#8a8a2a 40%,#c9a58c 60%,#2d3a1a)"></div>
  <div class="corner-dot"></div>
  <div style="position:absolute;left:192px;top:20px;width:153px">
    <p class="panel-head">Yoga Asana/Hand Mudra</p>
    <p class="panel-sub">Your headline here</p>
    <p class="body-copy" style="text-align:justify">• The physical postures of yoga replaces negative thinking and behaviors with physical movement and positive thinking.<br>• Hand Mudra's- are positions of the body, in most cases the hand, that allows for a change in mood or energy.<br>• Benefits:<br>• Allows patients to integrate mindful breathing and body awareness. Has the ability to heal an individual on every level of their being (emotionally, physically, mentally and spiritually) as well as promoting a healthy lifestyle and benefiting one's overall fitness.</p>
  </div>
  <div style="position:absolute;left:12px;top:108px;width:158px">
    <p class="panel-head" style="text-align:right">Research:</p>
    <p class="panel-sub" style="text-align:right">Your headline here</p>
    <p class="body-copy" style="text-align:justify">• A professor of medicine studied yoga and concluded that yoga could be overall more beneficial to ones well being than going for a brisk walk. Her research showed students emotionally happier, calm, confident, and in control as well as physically more fit. “Paying attention to your breathing is important during the strengthening part of rehab. And the mindfulness and greater awareness from meditation can help you cope with the stress of your illness, eat more healthfully, and sleep more soundly, all of which help your recovery,” she says.</p>
  </div>
  <p class="footer-mark">Business <span>Presentation</span></p>
</section>

</body>
</html>
```